TIDAL VERGE needs bisness cards pronto

Bisness name is "TIDAL VERGE" new bisness the bisness includes lawn mowing, garden matanace, and any jobs around the house.
I need a card that is colorful and vibrant and the bisness of lawn mowing maybe with some nature with it. It also needs my contact details"Darren Quellby mobile 0413562049 call for free quote and email norma.vance@fernmail.com.au and a catchy tag line

Industry/Entity Type

House

Requirements
Must have
• Bisness name "TIDAL VERGE"
Contact details "0413562049"
Email norma.vance@fernmail.com.au
Call for free quote

```html
<!DOCTYPE html>
<html lang="en">
<head>
<meta charset="utf-8">
<title>Tidal Verge – Business Cards</title>
<link rel="stylesheet" href="https://fonts.googleapis.com/css2?family=Oswald:wght@500;700&display=swap">
<style>
  :root {
    --backdrop: #d9d9d9;
    --card-black: #0b0b0b;
    --brand-red: #e3222b;
    --brand-green: #8dc63f;
    --grass-dark: #2f7a16;
    --grass-light: #5cae2c;
    --photo-tone: #3f7f6a;
  }
  * { box-sizing: border-box; margin: 0; padding: 0; }
  html, body { width: 1200px; height: 871px; overflow: hidden; }
  body {
    background: var(--backdrop);
    font-family: "Oswald", "Arial Narrow", sans-serif;
    position: relative;
  }
  .card {
    position: absolute;
    top: 280px;
    width: 540px;
    height: 310px;
    background: var(--card-black);
    overflow: hidden;
    box-shadow: 0 6px 18px rgba(0,0,0,.25);
  }
  .card--front { left: 40px; }
  .card--back { left: 620px; }
  .card__art { position: absolute; inset: 0; width: 100%; height: 100%; }

  /* Front */
  .front__brand {
    position: absolute;
    left: 90px; top: 112px;
    width: 380px;
  }
  .brand-name {
    font-weight: 700;
    color: var(--brand-red);
    letter-spacing: 1px;
    line-height: 1;
    text-transform: uppercase;
    white-space: nowrap;
  }
  .front__brand .brand-name { font-size: 52px; }
  .front__tagline {
    margin-top: 4px;
    font-weight: 500;
    font-size: 13px;
    color: var(--brand-green);
    letter-spacing: .5px;
    text-transform: uppercase;
    padding-left: 4px;
  }
  .front__rule {
    position: relative;
    margin-top: 6px;
    height: 2px;
    width: 330px;
    background: var(--brand-red);
  }
  .front__rule::after, .quote__rule::after {
    content: "";
    position: absolute;
    right: -12px; top: -4px;
    width: 10px; height: 10px;
    border-radius: 50%;
    background: var(--brand-red);
  }

  /* Back */
  .back__info {
    position: absolute;
    left: 225px; top: 50px;
    width: 290px;
    text-align: center;
  }
  .back__info .brand-name { font-size: 30px; }
  .quote {
    margin-top: 26px;
    font-weight: 700;
    font-size: 26px;
    color: var(--brand-red);
    text-transform: uppercase;
    line-height: 1;
    white-space: nowrap;
  }
  .quote__free { color: var(--brand-green); }
  .quote__rule {
    position: relative;
    margin: 8px auto 0;
    height: 2px;
    width: 250px;
    background: var(--brand-red);
  }
  .contact-name {
    margin-top: 24px;
    font-weight: 500;
    font-size: 20px;
    color: var(--brand-green);
    text-transform: uppercase;
    letter-spacing: .5px;
  }
  .contact-line {
    margin-top: 8px;
    font-weight: 500;
    font-size: 15px;
    color: var(--brand-green);
    text-transform: uppercase;
    letter-spacing: .3px;
    white-space: nowrap;
  }
  .contact-line .label { color: var(--brand-red); }
  .contact-line--email { font-size: 12.5px; margin-top: 4px; }
</style>
</head>
<body>

<section class="card card--front" aria-label="Card front">
  <svg class="card__art" viewBox="0 0 540 310" preserveAspectRatio="none">
    <defs>
      <linearGradient id="grassFill" x1="0" y1="0" x2="0" y2="1">
        <stop offset="0" stop-color="var(--grass-light)"/>
        <stop offset="1" stop-color="var(--grass-dark)"/>
      </linearGradient>
    </defs>
    <g role="img" aria-label="Close-up lawn grass texture">
      <polygon fill="url(#grassFill)" points="0,0 540,0 540,70 520,76 500,66 470,80 440,72 410,86 380,78 345,92 310,84 280,100 250,92 215,104 180,96 150,108 115,100 80,112 45,104 0,116"/>
      <polygon fill="url(#grassFill)" points="0,310 540,310 540,190 510,198 480,186 450,202 420,194 385,210 350,200 320,214 285,206 250,220 215,212 180,226 150,216 110,230 75,222 40,234 0,226"/>
    </g>
  </svg>
  <div class="front__brand">
    <p class="brand-name">Tidal Verge</p>
    <p class="front__tagline">For your professional cut lawns</p>
    <div class="front__rule"></div>
  </div>
</section>

<section class="card card--back" aria-label="Card back">
  <svg class="card__art" viewBox="0 0 540 310" preserveAspectRatio="none">
    <polygon class="photo-area" role="img" aria-label="Photo of a person mowing a lawn" fill="var(--photo-tone)" points="0,0 205,0 198,30 212,60 200,95 215,130 202,165 216,200 204,240 218,275 208,310 0,310"/>
  </svg>
  <div class="back__info">
    <p class="brand-name">Tidal Verge</p>
    <p class="quote">“Call for <span class="quote__free">free</span> quote”</p>
    <div class="quote__rule"></div>
    <p class="contact-name">Darren Quellby</p>
    <p class="contact-line"><span class="label">P:</span> 0413562049</p>
    <p class="contact-line contact-line--email"><span class="label">E:</span> norma.vance@fernmail.com.au</p>
  </div>
</section>

</body>
</html>
```